Real Estate Web Design

Hi

We are a real estate agency who is looking for a Corporate Design that would match our Style Guide. We have already developed the website but we want to apply our Branding on top of it. I am looking for some creative concepts

Below is our Test link for our new website
http://brightkeyhomes.sampledemo.com.au/

Attached is our Style Guide

Cheers
Ruvo

Industry/Entity Type

Real Estate

```html
<!DOCTYPE html>
<html lang="en">
<head>
<meta charset="utf-8">
<title>Brightkey Homes Management</title>
<link href="https://fonts.googleapis.com/css2?family=Source+Sans+3:ital,wght@0,400;0,600;0,700;1,400&display=swap" rel="stylesheet">
<style>
:root{
  --blue:#1d4f9e;
  --blue-dark:#163f80;
  --red:#e2302a;
  --text:#5a5a5a;
  --muted:#8a8a8a;
  --rule:#dcdcdc;
  --footer:#f1f1f1;
  --star:#f29a1f;
}
*{box-sizing:border-box;margin:0;padding:0}
html,body{width:1200px;height:2889px;overflow:hidden}
body{position:relative;background:#fff;font-family:"Source Sans 3",Arial,sans-serif;color:var(--text)}
.abs{position:absolute}

/* top bar */
.topbar{left:0;top:0;width:1200px;height:31px;background:var(--blue);color:#fff;font-size:10px;font-weight:600}
.topbar .mail{left:182px;top:9px;display:flex;align-items:center;gap:6px;text-transform:uppercase}
.topbar .social{left:706px;top:7px;display:flex;gap:6px}
.topbar .social span{width:17px;height:17px;border-radius:50%;background:#4f78bb;display:block}
.topbar .util{left:834px;top:9px;display:flex;gap:14px;text-transform:uppercase}
.topbar .util i{font-style:normal;opacity:.6}

/* header */
.logo{left:179px;top:48px;display:flex;align-items:center;gap:8px}
.logo .mark{width:20px;height:20px;background:var(--blue)}
.logo .name{font-size:26px;font-weight:700;color:var(--red);letter-spacing:-.5px}
.mainnav{top:58px;left:0;width:1200px;height:18px;font-size:13px;color:#333;text-transform:uppercase}
.mainnav a{position:absolute;top:0;color:inherit;text-decoration:none;white-space:nowrap}

/* hero */
.hero{left:0;top:100px;width:1200px;height:424px;background:linear-gradient(180deg,#8fa5bf 0%,#c7c1b4 45%,#8f826e 100%)}
.hero-arrow{top:180px;width:36px;height:36px;border-radius:50%;background:rgba(255,255,255,.3);border:1px solid rgba(255,255,255,.5)}
.video{left:154px;top:83px;width:495px;height:283px;border:6px solid #fff;background:linear-gradient(180deg,#9fc26a 0%,#e9d9b8 45%,#b6d07a 100%);box-shadow:0 2px 8px rgba(0,0,0,.3)}
.video .play{position:absolute;left:222px;top:116px;width:50px;height:36px;border-radius:7px;background:#222}
.search{left:732px;top:68px;width:324px;height:314px;background:rgba(255,255,255,.93);padding:20px 22px;font-size:11px;color:var(--blue);font-weight:600}
.search label{display:block;margin-bottom:6px}
.field{height:22px;border:1px solid #cfcfcf;background:#fff;font-size:9px;color:#999;padding:5px 6px;font-weight:400}
.field.select{display:flex;justify-content:space-between}
.field.select b{width:14px;height:14px;background:#555;margin-top:-2px}
.pair{display:grid;grid-template-columns:1fr 1fr;gap:10px}
.search .group{margin-bottom:14px}
.btn-red{display:block;margin-left:auto;width:122px;height:30px;background:var(--red);color:#fff;font-size:10px;text-align:center;line-height:30px;text-transform:uppercase;border-radius:2px}

/* intro columns */
.intro{top:558px;left:179px;width:842px;display:grid;grid-template-columns:repeat(3,256px);gap:37px}
.intro h3{font-size:12px;color:var(--blue);text-transform:uppercase;line-height:16px;height:40px;font-weight:700}
.intro .pic{height:130px;margin-bottom:12px}
.intro p{font-size:10px;line-height:15px;color:var(--text)}
.more{display:block;margin-top:8px;font-size:10px;color:var(--blue);font-weight:700}

.ad{height:77px}

.section-title{left:0;width:1200px;text-align:center;font-size:24px;color:var(--blue);font-weight:600}
.section-text{left:210px;width:780px;text-align:center;font-size:12.5px;line-height:25px;color:#555}
.rule{left:179px;width:842px;height:1px;background:var(--rule)}

/* listings */
.listings{left:179px;width:842px;display:grid;grid-template-columns:repeat(3,262px);gap:28px}
.card h4{font-size:11.5px;color:var(--blue);text-transform:uppercase;font-weight:700;height:23px;white-space:nowrap}
.card .pic{height:131px}
.card .meta{display:flex;padding:14px 10px 0;height:45px;border-bottom:1px solid #e8e8e8}
.card .who{width:50%;border-right:1px solid #e0e0e0;font-size:11px;color:var(--blue);font-weight:600}
.card .who small{display:flex;align-items:center;gap:4px;font-size:9px;color:#555;margin-top:3px;font-weight:600}
.card .rent{padding-left:14px;font-size:11.5px;color:var(--red);font-weight:700;line-height:13px}
.card .desc{font-size:10px;font-style:italic;color:#555;line-height:13px;padding:12px 0 0}
.card .age{display:flex;justify-content:space-between;font-size:9.5px;color:var(--muted);margin-top:7px}
.stars{color:var(--star);font-size:9px;letter-spacing:1px}
.stats{display:grid;grid-template-columns:repeat(3,1fr);border:1px solid #e2e2e2;margin-top:8px;height:37px;text-align:center}
.stats div{border-right:1px solid #e2e2e2;padding-top:4px;font-size:11px;color:var(--red);font-weight:700;line-height:14px}
.stats div:last-child{border-right:0}
.stats small{display:block;font-size:8.5px;color:var(--blue);text-transform:uppercase}

/* featured */
.featured{left:179px;top:2070px;width:846px;display:grid;grid-template-columns:repeat(4,195px);gap:22px}
.featured .pic{height:130px;margin-bottom:18px}
.featured h5{font-size:11px;color:var(--blue);text-transform:uppercase;line-height:17px;font-weight:700;width:170px}
.featured p{font-size:10px;line-height:15px;margin-top:8px}
.featured .more{margin-top:10px}

/* footer */
.footer{left:0;top:2479px;width:1200px;height:410px;background:var(--footer);border-top:1px solid #e2e2e2}
.footer h6{font-size:13px;color:var(--blue);text-transform:uppercase;font-weight:700;margin-bottom:10px}
.footer p,.footer li{font-size:10.5px;line-height:17px;color:#555;list-style:none}
.footer .col{position:absolute;top:34px}
.footer .readmore{text-align:right;display:block;margin-top:6px;font-size:10.5px}
.footer .contact li{display:flex;align-items:center;gap:6px}
.footer .line{position:absolute;left:0;top:183px;width:1200px;height:1px;background:#d8d8d8}
.footer .copy{position:absolute;left:179px;top:194px;font-size:10px;color:#777}
.skyline{position:absolute;left:0;bottom:0;width:1200px;height:200px;background:linear-gradient(180deg,rgba(195,200,208,0) 0%,#c9ced6 55%,#b9bfc9 100%)}
</style>
</head>
<body>

<header>
  <div class="abs topbar">
    <div class="abs mail">
      <svg width="11" height="8" viewBox="0 0 11 8"><rect x=".5" y=".5" width="10" height="7" fill="none" stroke="#fff"/><path d="M.5 .5 5.5 4.5 10.5 .5" fill="none" stroke="#fff"/></svg>
      Email us at : info@brightkeyhomesmanagement.com.au
    </div>
    <div class="abs social"><span></span><span></span><span></span><span></span><span></span></div>
    <nav class="abs util"><span>Home</span><i>|</i><span>About Us</span><i>|</i><span>Contact Us</span></nav>
  </div>
  <div class="abs logo"><span class="mark"></span><span class="name">Brightkey Homes</span></div>
  <nav class="abs mainnav"><a style="left:493px">Land Lords</a><a style="left:620px">Properties</a><a style="left:742px">Franchise Opportunitie</a><a style="left:938px">Testimonials</a></nav>
</header>

<section class="abs hero" role="img" aria-label="Blurred photo of a large two-storey house with balconies">
  <span class="abs hero-arrow" style="left:92px"></span>
  <span class="abs hero-arrow" style="left:1072px"></span>
  <div class="abs video" role="img" aria-label="Animated video still of cartoon houses with a property value counter">
    <span class="play"><svg width="50" height="36" viewBox="0 0 50 36"><path d="M20 11 32 18 20 25Z" fill="#fff"/></svg></span>
  </div>
  <form class="abs search">
    <div class="group"><label>Property Type :</label><div class="field select">- PROPERTY TYPE -<b></b></div></div>
    <div class="group"><label>Zip codes :</label><div class="field"></div></div>
    <div class="group pair">
      <div><label>Minimum Price :</label><div class="field">0</div></div>
      <div><label>Maximum Price :</label><div class="field">0</div></div>
    </div>
    <div class="group pair">
      <div><label>Bedrooms :</label><div class="field">0</div></div>
      <div><label>Maximum Price :</label><div class="field">0</div></div>
    </div>
    <span class="btn-red">List Properties</span>
  </form>
</section>

<section class="abs intro">
  <article>
    <h3>22 Harbour Lane, Bay Park WA 6230 Do you want your property managed?</h3>
    <div class="pic" role="img" aria-label="Photo of hands holding a small model house" style="background:linear-gradient(135deg,#3d6f9f,#e3b493 55%,#9a3d2c)"></div>
    <p>This comfortable family home with a large shed/workshop is well positioned close to shop ping This comfortable family home with a large shed/workshop is well positioned...</p>
    <span class="more">[ More Details + ]</span>
  </article>
  <article>
    <h3>How much rent can I get per week?</h3>
    <div class="pic" role="img" aria-label="Photo of a smiling man working at a laptop" style="background:linear-gradient(135deg,#c9b39a,#6f8fb5 60%,#dcd3c6)"></div>
    <p>This comfortable family home with a large shed/workshop is well positioned close to shop ping This comfortable family home with a large shed/workshop is well positioned...</p>
    <span class="more">[ More Details + ]</span>
  </article>
  <article>
    <h3>Franchise Opportunities</h3>
    <div class="pic" role="img" aria-label="Orange map of Australia divided into states" style="background:radial-gradient(ellipse at 50% 50%,#f39a2a 0%,#f5b25a 45%,#fff 72%)"></div>
    <p>This comfortable family home with a large shed/workshop is well positioned close to shop ping This comfortable family home with a large shed/workshop is well positioned...</p>
    <span class="more">[ More Details + ]</span>
  </article>
</section>

<div class="abs ad" role="img" aria-label="Advertising banner for discounted homes" style="left:277px;top:857px;width:624px;background:linear-gradient(90deg,#2d6a2a,#e6c21d 50%,#c22a1e)"></div>

<h2 class="abs section-title" style="top:958px">We are Offering the Best Real Estate Deals</h2>
<p class="abs section-text" style="top:997px">For the past 10 years in the South West we have been the leading specialist rental company. We have provided satisfaction to hundred's of landlords by getting the best tenant, paying the best rent in the shortest possible time.</p>
<div class="abs rule" style="top:1061px"></div>

<section class="abs listings" style="top:1086px">
  <article class="card"><h4>22 Harbour Lane, Bay Park WA 6230</h4>
    <div class="pic" role="img" aria-label="Photo of a single-storey house with a green lawn" style="background:linear-gradient(180deg,#8fb2d6,#e6e6e6 50%,#5f8d3c)"></div>
    <div class="meta"><div class="who">Lena Marsh<small><svg width="7" height="10" viewBox="0 0 7 10"><path d="M3.5 0A3.5 3.5 0 0 0 0 3.5C0 6 3.5 10 3.5 10S7 6 7 3.5A3.5 3.5 0 0 0 3.5 0Z" fill="#1d4f9e"/><circle cx="3.5" cy="3.5" r="1.3" fill="#fff"/></svg>CANADA</small></div><div class="rent">RENT : $ 270<br>/ MONTH</div></div>
    <p class="desc">Renovated Internally,3 large Bedrooms 1 Bathroom newly appointed rooms including Ceiling Fans,Polis...</p>
    <div class="age">12 days ago<span class="stars">★★★★☆</span></div>
    <div class="stats"><div>0<small>0 mtr sq</small></div><div>3<small>Bedrooms</small></div><div>1<small>Bathrooms</small></div></div>
  </article>
  <article class="card"><h4>22 Harbour Lane, Bay Park WA 6230</h4>
    <div class="pic" role="img" aria-label="Photo of a lit modern villa at dusk" style="background:linear-gradient(180deg,#2d4f8c,#c68a5a 55%,#3a2a2a)"></div>
    <div class="meta"><div class="who">Lena Marsh<small><svg width="7" height="10" viewBox="0 0 7 10"><path d="M3.5 0A3.5 3.5 0 0 0 0 3.5C0 6 3.5 10 3.5 10S7 6 7 3.5A3.5 3.5 0 0 0 3.5 0Z" fill="#1d4f9e"/><circle cx="3.5" cy="3.5" r="1.3" fill="#fff"/></svg>CANADA</small></div><div class="rent">RENT : $ 270<br>/ MONTH</div></div>
    <p class="desc">Renovated Internally,3 large Bedrooms 1 Bathroom newly appointed rooms including Ceiling Fans,Polis...</p>
    <div class="age">12 days ago<span class="stars">★★★★☆</span></div>
    <div class="stats"><div>0<small>0 mtr sq</small></div><div>3<small>Bedrooms</small></div><div>1<small>Bathrooms</small></div></div>
  </article>
  <article class="card"><h4>22 Harbour Lane, Bay Park WA 6230</h4>
    <div class="pic" role="img" aria-label="Photo of a house with a pool" style="background:linear-gradient(180deg,#7fa9d4,#b06a43 50%,#4fa0b8)"></div>
    <div class="meta"><div class="who">Lena Marsh<small><svg width="7" height="10" viewBox="0 0 7 10"><path d="M3.5 0A3.5 3.5 0 0 0 0 3.5C0 6 3.5 10 3.5 10S7 6 7 3.5A3.5 3.5 0 0 0 3.5 0Z" fill="#1d4f9e"/><circle cx="3.5" cy="3.5" r="1.3" fill="#fff"/></svg>CANADA</small></div><div class="rent">RENT : $ 270<br>/ MONTH</div></div>
    <p class="desc">Renovated Internally,3 large Bedrooms 1 Bathroom newly appointed rooms including Ceiling Fans,Polis...</p>
    <div class="age">12 days ago<span class="stars">★★★★☆</span></div>
    <div class="stats"><div>0<small>0 mtr sq</small></div><div>3<small>Bedrooms</small></div><div>1<small>Bathrooms</small></div></div>
  </article>
</section>

<section class="abs listings" style="top:1456px">
  <article class="card"><h4>22 Harbour Lane, Bay Park WA 6230</h4>
    <div class="pic" role="img" aria-label="Photo of a large white mansion" style="background:linear-gradient(180deg,#9ec0e0,#e8e0cf 50%,#7c8f58)"></div>
    <div class="meta"><div class="who">Lena Marsh<small><svg width="7" height="10" viewBox="0 0 7 10"><path d="M3.5 0A3.5 3.5 0 0 0 0 3.5C0 6 3.5 10 3.5 10S7 6 7 3.5A3.5 3.5 0 0 0 3.5 0Z" fill="#1d4f9e"/><circle cx="3.5" cy="3.5" r="1.3" fill="#fff"/></svg>CANADA</small></div><div class="rent">RENT : $ 270<br>/ MONTH</div></div>
    <p class="desc">Renovated Internally,3 large Bedrooms 1 Bathroom newly appointed rooms including Ceiling Fans,Polis...</p>
    <div class="age">12 days ago<span class="stars">★★★★☆</span></div>
    <div class="stats"><div>0<small>0 mtr sq</small></div><div>3<small>Bedrooms</small></div><div>1<small>Bathrooms</small></div></div>
  </article>
  <article class="card"><h4>22 Harbour Lane, Bay Park WA 6230</h4>
    <div class="pic" role="img" aria-label="Photo of a grey two-storey house" style="background:linear-gradient(180deg,#c7d3df,#5a5f66 50%,#6c8a4a)"></div>
    <div class="meta"><div class="who">Lena Marsh<small><svg width="7" height="10" viewBox="0 0 7 10"><path d="M3.5 0A3.5 3.5 0 0 0 0 3.5C0 6 3.5 10 3.5 10S7 6 7 3.5A3.5 3.5 0 0 0 3.5 0Z" fill="#1d4f9e"/><circle cx="3.5" cy="3.5" r="1.3" fill="#fff"/></svg>CANADA</small></div><div class="rent">RENT : $ 270<br>/ MONTH</div></div>
    <p class="desc">Renovated Internally,3 large Bedrooms 1 Bathroom newly appointed rooms including Ceiling Fans,Polis...</p>
    <div class="age">12 days ago<span class="stars">★★★★☆</span></div>
    <div class="stats"><div>0<small>0 mtr sq</small></div><div>3<small>Bedrooms</small></div><div>1<small>Bathrooms</small></div></div>
  </article>
  <article class="card"><h4>22 Harbour Lane, Bay Park WA 6230</h4>
    <div class="pic" role="img" aria-label="Photo of a brick house with a for sale sign" style="background:linear-gradient(180deg,#9fc3e6,#b48a5e 50%,#5b8a35)"></div>
    <div class="meta"><div class="who">Lena Marsh<small><svg width="7" height="10" viewBox="0 0 7 10"><path d="M3.5 0A3.5 3.5 0 0 0 0 3.5C0 6 3.5 10 3.5 10S7 6 7 3.5A3.5 3.5 0 0 0 3.5 0Z" fill="#1d4f9e"/><circle cx="3.5" cy="3.5" r="1.3" fill="#fff"/></svg>CANADA</small></div><div class="rent">RENT : $ 270<br>/ MONTH</div></div>
    <p class="desc">Renovated Internally,3 large Bedrooms 1 Bathroom newly appointed rooms including Ceiling Fans,Polis...</p>
    <div class="age">12 days ago<span class="stars">★★★★☆</span></div>
    <div class="stats"><div>0<small>0 mtr sq</small></div><div>3<small>Bedrooms</small></div><div>1<small>Bathrooms</small></div></div>
  </article>
</section>

<div class="abs rule" style="top:1818px"></div>
<div class="abs ad" role="img" aria-label="Advertising banner for a surface protection supplier" style="left:289px;top:1847px;width:624px;background:linear-gradient(90deg,#f2f2f2,#c8242a 30%,#f2f2f2 55%,#3a5aa6)"></div>

<h2 class="abs section-title" style="top:1944px">Featured Properties</h2>
<p class="abs section-text" style="top:1985px">For the past 10 years in the South West we have been the leading specialist rental company. We have provided satisfaction to hundred's of landlords by getting the best tenant, paying the best rent in the shortest possible time.</p>
<div class="abs rule" style="top:2045px"></div>

<section class="abs featured">
  <article><div class="pic" role="img" aria-label="Photo of a modern home lit at night by a pool" style="background:linear-gradient(180deg,#142a5c,#e6e9f2 55%,#2b6fb0)"></div>
    <h5>Family home in Eaton with large shed</h5><p>This comfortable family home with a large shed/workshop is well positioned close to shop ping centres...</p><span class="more">[ More Details + ]</span></article>
  <article><div class="pic" role="img" aria-label="Photo of a modern home entrance at dusk" style="background:linear-gradient(180deg,#2e3a55,#d8a36a 50%,#3a3630)"></div>
    <h5>Family home in Eaton with large shed</h5><p>This comfortable family home with a large shed/workshop is well positioned close to shop ping centres...</p><span class="more">[ More Details + ]</span></article>
  <article><div class="pic" role="img" aria-label="Photo of a dark modern home with lit windows" style="background:linear-gradient(180deg,#1c2438,#c78a4a 55%,#1f1f22)"></div>
    <h5>Family home in Eaton with large shed</h5><p>This comfortable family home with a large shed/workshop is well positioned close to shop ping centres...</p><span class="more">[ More Details + ]</span></article>
  <article><div class="pic" role="img" aria-label="Photo of a contemporary home with garage" style="background:linear-gradient(180deg,#9fb9d3,#8a8078 50%,#5e6e4a)"></div>
    <h5>Family home in Eaton with large shed</h5><p>This comfortable family home with a large shed/workshop is well positioned close to shop ping centres...</p><span class="more">[ More Details + ]</span></article>
</section>

<div class="abs ad" role="img" aria-label="Advertising banner for an investor conference" style="left:289px;top:2369px;width:626px;background:linear-gradient(90deg,#eef1f7,#2a3f8c 45%,#1b2d6e 80%,#f2c419)"></div>

<footer class="abs footer">
  <div class="col" style="left:179px;width:232px">
    <h6>About Us</h6>
    <p>You'll find just what you need with Brightkey Homes Management. Not only do we offer a completely unparalleled range of properties and locations, we're also the first choice for property...</p>
    <span class="readmore">[ Read more + ]</span>
  </div>
  <div class="col" style="left:447px">
    <h6>Quick Links</h6>
    <ul><li>Frequently asked Questions</li><li>How do I pay rent?</li><li>Tenant Policies</li><li>Tenants Information</li></ul>
  </div>
  <div class="col" style="left:618px;top:61px">
    <ul><li>Newsletter</li><li>Legal Information</li><li>Sitemap</li></ul>
  </div>
  <div class="col contact" style="left:776px">
    <h6>Contact Info</h6>
    <ul><li>First Floor</li><li>48 Marlin Street</li><li>Bayview WA 6230</li>
      <li><svg width="10" height="10" viewBox="0 0 10 10"><path d="M2 0 4 3 3 4C4 6 5 7 6 7L7 6 10 8 8 10C4 10 0 6 0 2Z" fill="#666"/></svg>Phone no :08 - 9000 - 4127</li>
      <li><svg width="10" height="8" viewBox="0 0 10 8"><rect width="10" height="8" fill="#666"/><path d="M0 0 5 4 10 0" fill="none" stroke="#fff"/></svg>Email us at : info@brightkeyhomesmanagement.com.au</li></ul>
  </div>
  <div class="line"></div>
  <span class="copy">© 2013 All Rights Reserved by Brightkey Homes</span>
  <div class="skyline" role="img" aria-label="Faint grey city skyline silhouette"></div>
</footer>

</body>
</html>
```